Create a new business card

I’m looking to update my business card to make it match the rest of my brand. I will include my current website as well as what my vehicle designs look like, etc..
What my business currently services
Weekly maintenance pool openings / closings
Equipment repair, including pumps, heaters, salt systems, filters, etc.
We install automatic covers and maintain them as well as provide preventative maintenance

I would like to include my name.
Darren Holcott.
My title
Owner
My email
Darren@tidewellnx.com
4015867120
Www.tidewellnx.com

```html
<!DOCTYPE html>
<html lang="en">
<head>
<meta charset="utf-8">
<title>Tidewell Pool Service – Business Card</title>
<link rel="stylesheet" href="https://fonts.googleapis.com/css2?family=Oswald:wght@500;600&family=Lato:wght@400&display=swap">
<style>
  :root {
    --navy: #213266;
    --sky: #29abe2;
    --white: #ffffff;
    --backdrop: #eef0f2;
    --shadow: rgba(0, 0, 0, 0.18);
  }
  * { margin: 0; padding: 0; box-sizing: border-box; }
  html, body { width: 1200px; height: 1200px; overflow: hidden; }
  body { background: var(--backdrop); position: relative; font-family: "Lato", sans-serif; }

  .card {
    position: absolute;
    left: 159px;
    width: 881px;
    height: 514px;
    background: var(--white);
    box-shadow: 0 3px 10px var(--shadow);
    overflow: hidden;
  }
  .card--front { top: 65px; }
  .card--back { top: 622px; }

  .splash { position: absolute; inset: 0; width: 100%; height: 100%; }

  .identity {
    position: absolute;
    left: 62px;
    top: 258px;
    color: var(--white);
  }
  .identity__name {
    font-family: "Oswald", sans-serif;
    font-weight: 600;
    font-size: 44px;
    line-height: 1;
    letter-spacing: 0.2px;
  }
  .identity__title {
    font-family: "Oswald", sans-serif;
    font-weight: 500;
    font-size: 26px;
    margin-top: 10px;
  }
  .contacts { list-style: none; margin-top: 24px; }
  .contacts li {
    display: flex;
    align-items: center;
    gap: 12px;
    font-size: 21px;
    line-height: 34px;
  }
  .contacts svg { width: 14px; height: 14px; fill: var(--white); flex: none; }

  .brand {
    position: absolute;
    display: flex;
    align-items: center;
    gap: 12px;
    color: var(--navy);
    font-family: "Oswald", sans-serif;
    font-weight: 600;
    line-height: 1.05;
    text-align: left;
  }
  .brand__dot {
    flex: none;
    border-radius: 50%;
    background: var(--sky);
  }
  .brand--front { left: 608px; top: 128px; font-size: 34px; }
  .brand--front .brand__dot { width: 28px; height: 28px; }
  .brand--back { left: 112px; top: 206px; font-size: 44px; }
  .brand--back .brand__dot { width: 36px; height: 36px; }
</style>
</head>
<body>

<section class="card card--front">
  <svg class="splash" viewBox="0 0 881 514" preserveAspectRatio="none" role="img" aria-label="Navy water splash texture sweeping diagonally across the card">
    <defs>
      <linearGradient id="front-water" x1="0" y1="1" x2="1" y2="0">
        <stop offset="0.62" stop-color="#213266"/>
        <stop offset="0.75" stop-color="#29abe2"/>
      </linearGradient>
    </defs>
    <polygon points="0,0 110,0 300,150 440,320 570,330 720,430 881,470 881,514 0,514" fill="url(#front-water)"/>
    <polygon points="0,0 95,0 280,150 410,320 560,345 700,440 881,490 881,514 0,514" fill="#213266"/>
  </svg>

  <div class="identity">
    <h1 class="identity__name">Darren Holcott</h1>
    <p class="identity__title">Owner</p>
    <ul class="contacts">
      <li>
        <svg viewBox="0 0 16 16" aria-hidden="true"><path d="M3.6 1.2 6 3.6 4.6 5.4c.9 2 2.4 3.5 4.4 4.4l1.6-1.4 2.4 2.4-1.5 2.3C7 13 3 9 2.2 2.8Z"/></svg>
        <span>4015867120</span>
      </li>
      <li>
        <svg viewBox="0 0 16 16" aria-hidden="true"><path d="M1 3h14v10H1Zm1.4 1.2L8 8.6l5.6-4.4Z"/></svg>
        <span>Darren@tidewellnx.com</span>
      </li>
      <li>
        <svg viewBox="0 0 16 16" aria-hidden="true"><path d="M8 1a7 7 0 1 0 0 14A7 7 0 0 0 8 1Zm0 1.6c.9 1 1.5 2.6 1.7 4.6H6.3C6.5 5.2 7.1 3.6 8 2.6ZM6.3 8.8h3.4c-.2 2-.8 3.6-1.7 4.6-.9-1-1.5-2.6-1.7-4.6ZM2.7 7.2a5.4 5.4 0 0 1 2.6-4c-.4 1.1-.7 2.5-.8 4Zm0 1.6h1.8c.1 1.5.4 2.9.8 4a5.4 5.4 0 0 1-2.6-4Zm8 4c.4-1.1.7-2.5.8-4h1.8a5.4 5.4 0 0 1-2.6 4Zm.8-5.6c-.1-1.5-.4-2.9-.8-4a5.4 5.4 0 0 1 2.6 4Z"/></svg>
        <span>www.tidewellnx.com</span>
      </li>
    </ul>
  </div>

  <div class="brand brand--front">
    <span class="brand__dot"></span>
    <span>Tidewell<br>Pool Service</span>
  </div>
</section>

<section class="card card--back">
  <svg class="splash" viewBox="0 0 881 514" preserveAspectRatio="none" role="img" aria-label="Blue rippling pool water texture along the right edge">
    <defs>
      <linearGradient id="back-water" x1="0" y1="0" x2="1" y2="0">
        <stop offset="0" stop-color="#ffffff"/>
        <stop offset="0.35" stop-color="#29abe2"/>
        <stop offset="0.8" stop-color="#29abe2"/>
        <stop offset="1" stop-color="#213266"/>
      </linearGradient>
    </defs>
    <rect x="520" y="0" width="361" height="514" fill="url(#back-water)"/>
  </svg>

  <div class="brand brand--back">
    <span class="brand__dot"></span>
    <span>Tidewell<br>Pool Service</span>
  </div>
</section>

</body>
</html>
```